Corporate Identity Design for Travel Company

We need a brand book, that should include the following artwork:

Business card
Letterhead
Envelope (DL, C4, C5)
A4 folder
A4 paper for notes
E-mail signature
Power point template
Pen design

Please, submit your designs that include business card, letterhead and envelope. Once selected the winner, he will be asked to complete the project by creating the rest of the artwork.

Logo and project requirements are attached.

```html
<!DOCTYPE html>
<html lang="en">
<head>
<meta charset="utf-8">
<title>Four Season Routes – Stationery Set</title>
<link rel="stylesheet" href="https://fonts.googleapis.com/css2?family=Marcellus&family=Marcellus+SC&family=Great+Vibes&display=swap">
<style>
  :root {
    --paper: #ffffff;
    --card-cream: #f9f4c9;
    --card-frame: #8dc153;
    --ink-grey: #555a52;
    --ink-dark: #1b1b1b;
    --brand-green: #6bb24a;
    --swirl-peach: #f2b47a;
    --swirl-yellow: #eadf72;
  }
  * { margin: 0; padding: 0; box-sizing: border-box; }
  html, body { width: 1200px; height: 2824px; overflow: hidden; background: var(--paper); }
  .sheet { position: relative; width: 1200px; height: 2824px; }

  /* Business card */
  .business-card {
    position: absolute; left: 102px; top: 0; width: 988px; height: 565px;
    background: var(--card-cream);
    border: 5px solid var(--card-frame);
    overflow: hidden;
  }
  .business-card .card-decoration {
    position: absolute; right: 0; top: 0; width: 400px; height: 100%;
    background: radial-gradient(ellipse at 60% 55%, rgba(242,180,122,0.55), rgba(234,223,114,0.25) 55%, rgba(249,244,201,0) 80%);
  }
  .brand { position: absolute; display: flex; align-items: center; font-family: "Marcellus", serif; color: var(--ink-grey); }
  .brand-square { background: var(--brand-green); border-radius: 14%; flex: none; }
  .brand-name { line-height: 0.98; }
  .business-card .brand { left: 26px; top: 22px; }
  .business-card .brand-square { width: 176px; height: 176px; margin-right: 30px; }
  .business-card .brand-name { font-size: 78px; }

  .card-contact {
    position: absolute; left: 0; top: 272px; width: 600px; text-align: center;
    color: var(--ink-grey); font-family: "Marcellus SC", serif;
  }
  .card-contact .holder-name { font-family: "Great Vibes", cursive; font-size: 66px; line-height: 1; margin-bottom: 2px; }
  .card-contact .holder-title { font-size: 44px; letter-spacing: 5px; line-height: 1.1; }
  .card-contact .holder-email { font-size: 32px; letter-spacing: 4px; line-height: 1.3; }
  .card-contact .holder-phone { font-family: "Marcellus", serif; font-size: 30px; letter-spacing: 3px; line-height: 1.2; }
  .card-contact .holder-address { font-size: 28px; letter-spacing: 2px; line-height: 1.12; }

  /* Small brand block on letterhead & envelope */
  .brand-block { position: absolute; width: 240px; }
  .brand-block .brand { position: static; }
  .brand-block .brand-square { width: 76px; height: 76px; margin-right: 12px; }
  .brand-block .brand-name { font-size: 33px; }
  .brand-block .brand-address {
    font-family: "Marcellus SC", serif; font-size: 11px; color: var(--ink-grey);
    text-align: center; line-height: 1.25; letter-spacing: 0.5px; margin-top: 4px;
  }
  .letterhead-brand { left: 131px; top: 843px; }
  .envelope-brand { left: 16px; top: 2318px; }

  /* Envelope */
  .envelope-decoration {
    position: absolute; left: 1068px; top: 2136px; width: 128px; height: 138px;
    background: radial-gradient(ellipse at 55% 55%, rgba(242,180,122,0.45), rgba(234,223,114,0.2) 60%, rgba(255,255,255,0) 80%);
  }
  .postage-box {
    position: absolute; left: 1109px; top: 2302px; width: 69px; height: 83px;
    background: var(--brand-green);
    display: flex; align-items: center; justify-content: center;
    font-family: "Marcellus SC", serif; font-size: 11px; color: var(--ink-dark);
  }
  .recipient {
    position: absolute; left: 392px; top: 2606px; width: 400px; text-align: center;
    font-family: "Marcellus SC", serif; font-weight: 400; font-size: 22px; letter-spacing: 2px;
    line-height: 1.3; color: var(--ink-dark);
  }
</style>
</head>
<body>
<main class="sheet">

  <section class="business-card">
    <div class="card-decoration" role="img" aria-label="Flowing orange and yellow swirl ornament"></div>
    <div class="brand">
      <span class="brand-square"></span>
      <span class="brand-name">Four Season<br>Routes</span>
    </div>
    <div class="card-contact">
      <p class="holder-name">John Doe</p>
      <p class="holder-title">Position/Title</p>
      <p class="holder-email">email@address.com</p>
      <p class="holder-phone">555-555-555</p>
      <p class="holder-address">1234 Corporate Dr. suite 201<br>City, State 12345</p>
    </div>
  </section>

  <section class="brand-block letterhead-brand">
    <div class="brand">
      <span class="brand-square"></span>
      <span class="brand-name">Four Season<br>Routes</span>
    </div>
    <p class="brand-address">1234 Corporate Dr. Suite 201<br>City, State 12345<br>555-555-5555</p>
  </section>

  <div class="envelope-decoration" role="img" aria-label="Small orange swirl ornament"></div>
  <section class="brand-block envelope-brand">
    <div class="brand">
      <span class="brand-square"></span>
      <span class="brand-name">Four Season<br>Routes</span>
    </div>
    <p class="brand-address">1234 Corporate Dr. Suite 201<br>City, State 12345<br>555-555-5555</p>
  </section>
  <div class="postage-box">Postage</div>
  <address class="recipient" style="font-style: normal;">Jane Doe<br>1234 A Street<br>City, State 12345</address>

</main>
</body>
</html>
```